Creative & Professional Business Card for hair salon

We are looking to update our business cards. Our salon is creative, modern, progressive and professional and looking for a design that will reflect this.

```html
<!DOCTYPE html>
<html lang="en">
<head>
<meta charset="utf-8">
<title>Silver Strands – Business Card</title>
<link rel="stylesheet" href="https://fonts.googleapis.com/css2?family=Arimo&family=Quicksand:wght@300&family=Source+Sans+3:wght@400;700&display=swap">
<style>
  :root {
    --page: #ffffff;
    --card: #ffffff;
    --card-edge: #d9d9d9;
    --ink: #111111;
    --slate: #3f6079;
    --icon-ring: #3b4e7a;
  }
  * { margin: 0; padding: 0; box-sizing: border-box; }
  html, body { width: 1200px; height: 1200px; overflow: hidden; background: var(--page); }
  .canvas { position: relative; width: 1200px; height: 1200px; }

  .card {
    position: absolute;
    left: 180px;
    width: 840px;
    height: 480px;
    background: var(--card);
    overflow: hidden;
  }
  .card--back { top: 99px; border-bottom: 1px solid var(--card-edge); }
  .card--front { top: 612px; border: 1px solid var(--card-edge); border-left: none; }

  .artwork { position: absolute; top: 0; height: 100%; }
  .card--back .artwork { left: 380px; width: 460px; }
  .card--front .artwork { left: 0; width: 560px; }

  .contact-list { position: absolute; left: 0; top: 0; list-style: none; }
  .contact-item {
    position: absolute;
    left: 40px;
    height: 56px;
    display: flex;
    align-items: center;
    white-space: nowrap;
    font-family: "Arimo", Arial, sans-serif;
    font-size: 24px;
    color: var(--ink);
  }
  .contact-icon { width: 56px; height: 56px; margin-right: 44px; flex: none; }

  .brand {
    position: absolute;
    right: 48px;
    top: 290px;
    text-align: right;
    font-family: "Quicksand", sans-serif;
    font-weight: 300;
    color: var(--slate);
  }
  .brand-name { font-size: 46px; line-height: 1; letter-spacing: -0.5px; }
  .brand-by { font-size: 22px; margin-top: 8px; }

  .tagline {
    position: absolute;
    right: 48px;
    top: 406px;
    font-family: "Source Sans 3", sans-serif;
    font-size: 27px;
    color: var(--slate);
    letter-spacing: 0.2px;
  }
  .tagline b { font-weight: 700; }
</style>
</head>
<body>
<main class="canvas">

  <section class="card card--back">
    <svg class="artwork" viewBox="0 0 460 480" preserveAspectRatio="none" role="img" aria-label="Area for a watercolour portrait photograph with rainbow-splashed hair">
      <defs>
        <linearGradient id="toneBack" x1="0" y1="0" x2="1" y2="1">
          <stop offset="0" stop-color="#7a9ad6"/>
          <stop offset="0.35" stop-color="#7cc08f"/>
          <stop offset="0.6" stop-color="#efe08a"/>
          <stop offset="1" stop-color="#ee8a8f"/>
        </linearGradient>
        <linearGradient id="fadeBack" x1="0" y1="0" x2="1" y2="0">
          <stop offset="0" stop-color="#fff" stop-opacity="1"/>
          <stop offset="0.45" stop-color="#fff" stop-opacity="0.35"/>
          <stop offset="1" stop-color="#fff" stop-opacity="0.2"/>
        </linearGradient>
      </defs>
      <rect width="460" height="480" fill="url(#toneBack)"/>
      <rect width="460" height="480" fill="url(#fadeBack)"/>
    </svg>

    <ul class="contact-list">
      <li class="contact-item" style="top:42px">
        <svg class="contact-icon" viewBox="0 0 52 52" aria-hidden="true"><circle cx="26" cy="26" r="22" fill="var(--icon-ring)"/><circle cx="26" cy="20" r="6" fill="#fff"/><path d="M15 37 C16 29 36 29 37 37 Z" fill="#fff"/></svg>
        Marco Bellini
      </li>
      <li class="contact-item" style="top:112px">
        <svg class="contact-icon" viewBox="0 0 52 52" aria-hidden="true"><circle cx="26" cy="26" r="22" fill="var(--icon-ring)"/><path d="M26 38 C20 30 18 26 18 22 A8 8 0 0 1 34 22 C34 26 32 30 26 38 Z" fill="#fff"/><circle cx="26" cy="22" r="3" fill="var(--icon-ring)"/></svg>
        27 Wattle Lane, Coolwater
      </li>
      <li class="contact-item" style="top:176px">
        <svg class="contact-icon" viewBox="0 0 52 52" aria-hidden="true"><circle cx="26" cy="26" r="22" fill="var(--icon-ring)"/><rect x="17" y="14" width="18" height="24" rx="3" fill="#fff"/><path d="M22 20 L25 20 L26 24 L24 25 C25 28 26 29 28 30 L29 28 L32 29 L32 32 C26 33 21 27 22 20 Z" fill="var(--icon-ring)"/></svg>
        07 5123 4567
      </li>
      <li class="contact-item" style="top:244px">
        <svg class="contact-icon" viewBox="0 0 52 52" aria-hidden="true"><circle cx="26" cy="26" r="22" fill="var(--icon-ring)"/><rect x="14" y="18" width="24" height="17" rx="2" fill="#fff"/><path d="M14 19 L26 28 L38 19" fill="none" stroke="var(--icon-ring)" stroke-width="2"/></svg>
        salon@silverstrands.com.au
      </li>
      <li class="contact-item" style="top:311px">
        <svg class="contact-icon" viewBox="0 0 52 52" aria-hidden="true"><circle cx="26" cy="26" r="22" fill="var(--icon-ring)"/><g fill="none" stroke="#fff" stroke-width="1.8"><circle cx="26" cy="26" r="11"/><ellipse cx="26" cy="26" rx="5" ry="11"/><path d="M15 26 H37 M17 20 H35 M17 32 H35"/></g></svg>
        www.silverstrands.com.au
      </li>
      <li class="contact-item" style="top:377px">
        <svg class="contact-icon" viewBox="0 0 52 52" aria-hidden="true"><circle cx="26" cy="26" r="22" fill="var(--icon-ring)"/><path d="M15 17 H37 A2 2 0 0 1 39 19 V31 A2 2 0 0 1 37 33 H24 L18 38 V33 H15 A2 2 0 0 1 13 31 V19 A2 2 0 0 1 15 17 Z" fill="#fff"/></svg>
        SilverStrandsbyMarcoBellini
      </li>
    </ul>
  </section>

  <section class="card card--front">
    <svg class="artwork" viewBox="0 0 560 480" preserveAspectRatio="none" role="img" aria-label="Area for a watercolour portrait photograph with rainbow-splashed hair">
      <defs>
        <linearGradient id="toneFront" x1="0" y1="0" x2="1" y2="1">
          <stop offset="0" stop-color="#ee8a8f"/>
          <stop offset="0.4" stop-color="#efe08a"/>
          <stop offset="0.65" stop-color="#7cc08f"/>
          <stop offset="1" stop-color="#7a9ad6"/>
        </linearGradient>
        <linearGradient id="fadeFront" x1="0" y1="0" x2="1" y2="0">
          <stop offset="0" stop-color="#fff" stop-opacity="0.2"/>
          <stop offset="0.55" stop-color="#fff" stop-opacity="0.35"/>
          <stop offset="1" stop-color="#fff" stop-opacity="1"/>
        </linearGradient>
      </defs>
      <rect width="560" height="480" fill="url(#toneFront)"/>
      <rect width="560" height="480" fill="url(#fadeFront)"/>
    </svg>

    <div class="brand">
      <div class="brand-name">Silver Strands</div>
      <div class="brand-by">by Marco Bellini</div>
    </div>

    <p class="tagline"><b>creative</b>modern<b>progressive</b>professional</p>
  </section>

</main>
</body>
</html>
```